red gum junk haulage

A 6 flyer design.......
I have up loaded our company logo ....must use
A location map...........must use
and our business card with our contact information......please add all contact info
our ph. number must bold and prominent feature.....use use

A reliable Asbestos Removal & Demolition service that you can trust. All our services are offered at realistic prices and delivered on time. We operate 24 / 7 and provide free no-obligation quotes with good old fashion service.

We service the following towns and surrounding areas 7
days a week & 24 hours
Kempsey
Taree
South West Rocks
foster / Tuncurry
Coffs harbour
Nambucca Heads
Newcastle
Maitland
Singleton
Muswellbrook
Upper Hunter Valley
Central Coast
Tamworth
Armidale
this is an easy design as I have most of the theme and colours

```html
<!DOCTYPE html>
<html lang="en">
<head>
<meta charset="utf-8">
<title>Red Gum Junk Haulage – Flyer</title>
<link href="https://fonts.googleapis.com/css2?family=Roboto:wght@300;400;500;700;900&display=swap" rel="stylesheet">
<style>
  :root {
    --page-bg: #ffffff;
    --metal-light: #ececec;
    --metal-mid: #c9c9c9;
    --metal-dark: #a9a9a9;
    --band-dark: #8f9092;
    --band-mid: #b4b5b7;
    --ink: #222222;
    --ink-soft: #333333;
    --brand-yellow: #f7d900;
    --brand-green: #138a3c;
    --map-land: #d9e4c4;
    --map-sea: #a9cdf3;
  }
  * { margin: 0; padding: 0; box-sizing: border-box; }
  html, body {
    width: 1200px; height: 1000px; overflow: hidden;
    background: var(--page-bg);
    font-family: "Roboto", Arial, sans-serif;
    color: var(--ink);
  }
  .flyer {
    position: absolute; left: 307px; top: 60px;
    width: 620px; height: 873px;
    background: radial-gradient(ellipse at 50% 40%, var(--metal-light) 0%, var(--metal-mid) 60%, var(--metal-dark) 100%);
    box-shadow: 3px 4px 5px rgba(0,0,0,0.45);
    overflow: hidden;
  }
  .brand {
    position: absolute; left: 0; width: 100%; top: 48px;
    text-align: center; color: var(--brand-green);
    font-weight: 900; text-transform: uppercase; line-height: 1;
  }
  .brand-line-1 { display: block; font-size: 66px; letter-spacing: 1px; }
  .brand-line-2 { display: block; font-size: 44px; margin-top: 8px; }
  .tagline {
    position: absolute; left: 0; width: 100%; top: 206px;
    text-align: center; font-weight: 700; font-size: 21.5px;
    line-height: 31px; text-transform: uppercase; color: var(--ink);
  }
  .contact-band {
    position: absolute; left: 0; top: 288px; width: 100%; height: 154px;
    background: linear-gradient(90deg, var(--band-dark) 0%, var(--band-mid) 50%, var(--band-dark) 100%);
    text-align: center;
  }
  .phone {
    margin-top: 12px;
    font-size: 50px; font-weight: 900; letter-spacing: 3px;
    color: var(--brand-yellow);
    -webkit-text-stroke: 2px var(--brand-green);
    paint-order: stroke fill;
  }
  .contact-line {
    font-size: 19.5px; font-weight: 500; letter-spacing: 1px;
    color: var(--ink); line-height: 36px;
  }
  .contact-line.email { margin-top: 2px; }
  .intro {
    position: absolute; left: 0; width: 100%; top: 462px;
    text-align: center; font-weight: 300; font-size: 19px;
    line-height: 32px; color: var(--ink-soft);
  }
  .intro strong { font-weight: 700; }
  .areas-heading {
    position: absolute; left: 0; width: 100%; top: 585px;
    text-align: center; font-weight: 500; font-size: 16.5px;
    line-height: 25px; color: var(--brand-green);
  }
  .area-map {
    position: absolute; left: 73px; top: 654px; width: 166px; height: 166px;
    background: linear-gradient(90deg, var(--map-land) 0%, var(--map-land) 72%, var(--map-sea) 80%, var(--map-sea) 100%);
  }
  .town-list {
    position: absolute; top: 655px; list-style: none;
    font-size: 14.5px; font-weight: 500; line-height: 23.3px; color: var(--ink-soft);
  }
  .town-list.first { left: 263px; }
  .town-list.second { left: 414px; }
</style>
</head>
<body>
  <main class="flyer">
    <h1 class="brand">
      <span class="brand-line-1">Red Gum</span>
      <span class="brand-line-2">Junk Haulage</span>
    </h1>

    <p class="tagline">A reliable asbestos removal &amp;<br>demolition service that you can trust!</p>

    <section class="contact-band">
      <p class="phone">TEL: 0412556890</p>
      <p class="contact-line email">hello@redgumjunkhaulage.com</p>
      <p class="contact-line web">www.redgumjunkhaulage.com</p>
    </section>

    <p class="intro">All our services are offered at realistic prices and<br>delivered on time. We operate 24/7 and provide <strong>FREE</strong><br>no-obligation quotes with good old fashion service.</p>

    <p class="areas-heading">We service the following towns and surrounding areas<br>7 days a week and 24 hours:</p>

    <div class="area-map" role="img" aria-label="Location map of the NSW coast showing the service area radius"></div>

    <ul class="town-list first">
      <li>Kempsey</li>
      <li>Taree</li>
      <li>South West Rocks</li>
      <li>Foster / Tuncurry</li>
      <li>Coffs Harbour</li>
      <li>Nambucca Heads</li>
      <li>Newcastle</li>
    </ul>
    <ul class="town-list second">
      <li>Maitland</li>
      <li>Singleton</li>
      <li>Muswellbrook</li>
      <li>Upper Hunter Valley</li>
      <li>Central Coast</li>
      <li>Tamworth</li>
      <li>Armidale</li>
    </ul>
  </main>
</body>
</html>
```